Sympathy Gift Supplier needs packaging designs

We provide sympathy/bereavement gifts such as memorial candles and picture frames for those who recently lost a loved one. We need packaging design for our boxes that will be uplifting and positive, yet elegant.

We have attached our logo in white and black as well as a saying we would like on the box, and what we need on the back panel.
Ignore the black as it was something we were working on for another product.

These products will be given as gifts to people who lost a loved one as remembrance.

• Back panel details (provided)
Memorial quote (provided)
Must be appropriate for this type of product

```html
<!DOCTYPE html>
<html lang="en">
<head>
<meta charset="utf-8">
<title>Serene Grove – Memorial Candle Box Panels</title>
<link rel="stylesheet" href="https://fonts.googleapis.com/css2?family=Jost:wght@400;500&family=Cormorant+Garamond:ital@1&display=swap">
<style>
  :root {
    --backdrop: #e6e7e9;
    --panel-navy: #101527;
    --leaf-green: #8dc63f;
    --plum: #6a2c91;
    --soft-plum: #8a52b3;
    --ink-white: #ffffff;
  }
  * { box-sizing: border-box; margin: 0; padding: 0; }
  html, body {
    width: 1200px; height: 1199px; overflow: hidden;
    background: var(--backdrop);
    font-family: "Jost", "Futura", sans-serif;
  }
  .panel {
    position: absolute; width: 655px; height: 506px;
    background: var(--panel-navy); overflow: hidden;
  }
  .panel--front { left: 133px; top: 86px; }
  .panel--back  { left: 413px; top: 607px; }
  .frame { position: absolute; inset: 0; width: 655px; height: 506px; }

  .quote {
    position: absolute; left: 0; right: 0; top: 130px;
    text-align: center; color: var(--ink-white);
    font-size: 23px; line-height: 36px; letter-spacing: 0.5px;
  }
  .quote .small { font-size: 19px; }
  .quote .love { color: var(--plum); font-weight: 500; font-size: 40px; }
  .quote-script {
    position: absolute; left: 0; right: 0; top: 252px; text-align: center;
    font-family: "Cormorant Garamond", serif; font-style: italic;
    color: var(--plum); font-size: 50px;
  }

  .brand-mark {
    position: absolute; left: 0; right: 0;
    display: flex; align-items: center; justify-content: center; gap: 10px;
    font-family: "Jost", sans-serif; font-weight: 400; color: var(--leaf-green);
  }
  .brand-mark .dot { width: 14px; height: 14px; border-radius: 50%; background: var(--plum); }
  .panel--front .brand-mark { top: 385px; font-size: 30px; }
  .panel--back .brand-mark { top: 385px; font-size: 24px; }

  .care-info {
    position: absolute; left: 0; right: 0; top: 138px; text-align: center;
  }
  .divider { display: block; margin: 0 auto 4px; }
  .care-heading { color: var(--plum); font-weight: 500; font-size: 11px; letter-spacing: 0.3px; }
  .care-heading--warning { font-size: 12px; }
  .care-text { color: var(--leaf-green); font-size: 7.5px; line-height: 12px; margin: 4px 0 6px; }
  .origin { color: var(--soft-plum); font-weight: 500; font-size: 11px; letter-spacing: 3px; margin-top: 2px; }
  .brand-line {
    font-family: "Cormorant Garamond", serif; font-style: italic;
    color: var(--leaf-green); font-size: 26px; margin: 4px 0 2px;
  }
  .tagline { color: var(--ink-white); font-size: 9.5px; line-height: 13px; }

  .web-tab {
    position: absolute; left: 224px; width: 205px; bottom: 0; height: 34px;
    background: var(--leaf-green); border-radius: 12px 12px 0 0;
    display: flex; align-items: center; justify-content: center;
    color: var(--panel-navy); font-size: 10px; letter-spacing: 1.6px;
  }
</style>
</head>
<body>

<svg width="0" height="0" style="position:absolute">
  <defs>
    <linearGradient id="scrollTone" x1="0" y1="0" x2="0" y2="1">
      <stop offset="0" stop-color="#8dc63f" stop-opacity="0.35"/>
      <stop offset="1" stop-color="#8dc63f" stop-opacity="0.08"/>
    </linearGradient>
    <g id="panelFrame" fill="none" stroke="#8dc63f" stroke-linecap="round">
      <path d="M50 120 Q60 88 120 86 Q230 78 327 102 Q424 78 535 86 Q595 88 605 120" stroke-width="4"/>
      <path d="M50 120 L50 430 Q52 460 110 462" stroke-width="3"/>
      <path d="M605 120 L605 430 Q603 460 545 462" stroke-width="3"/>
      <path d="M66 140 L66 410" stroke-width="1.5"/>
      <path d="M589 140 L589 410" stroke-width="1.5"/>
    </g>
  </defs>
</svg>

<section class="panel panel--front" aria-label="Front panel">
  <svg class="frame" viewBox="0 0 655 506" aria-hidden="true">
    <use href="#panelFrame"/>
  </svg>
  <svg class="frame" viewBox="0 0 655 506">
    <rect role="img" aria-label="Green flourish ornament crowning the frame" x="150" y="22" width="355" height="60" rx="30" fill="url(#scrollTone)"/>
  </svg>
  <p class="quote">
    <span class="small">WHEN THE PEOPLE WE</span> <span class="love">LOVE</span> <span class="small">ARE</span><br>
    TAKEN <span class="small">FROM US, THE WAY TO HAVE</span><br>
    <span class="small">THEM LIVE ON IS TO</span> NEVER STOP
  </p>
  <p class="quote-script">Loving Them.</p>
  <div class="brand-mark"><span class="dot"></span>Serene Grove</div>
</section>

<section class="panel panel--back" aria-label="Back panel">
  <svg class="frame" viewBox="0 0 655 506" aria-hidden="true">
    <use href="#panelFrame"/>
  </svg>
  <svg class="frame" viewBox="0 0 655 506">
    <rect role="img" aria-label="Green flourish ornament crowning the frame" x="150" y="22" width="355" height="60" rx="30" fill="url(#scrollTone)"/>
  </svg>

  <div class="care-info">
    <svg class="divider" width="360" height="14" viewBox="0 0 360 14" aria-hidden="true">
      <g stroke="#8dc63f" fill="#8dc63f">
        <line x1="10" y1="7" x2="150" y2="7" stroke-width="1"/>
        <line x1="210" y1="7" x2="350" y2="7" stroke-width="1"/>
        <circle cx="8" cy="7" r="2.5"/><circle cx="352" cy="7" r="2.5"/>
        <circle cx="180" cy="7" r="4" fill="none" stroke-width="1.5"/>
      </g>
    </svg>
    <p class="care-heading care-heading--warning">WARNING</p>
    <p class="care-text">Burn within sight. Keep away from flammable objects. Keep away from children and pets.</p>
    <p class="care-heading">Burning Instructions:</p>
    <p class="care-text">Trim wick to 1/4" before lighting. Keep candle free of any foreign materials including matches and<br>
    wick trimmings. Only burn the candle on a level, fire resistant surface.<br>
    Do not burn candle for more than four hours at a time. Stop use when only 1/4" of wax remains.</p>
    <p class="origin">MADE IN CHINA</p>
    <p class="brand-line">Serene Grove</p>
    <p class="tagline">IS A FAMILY OWNED COMPANY<br>AND ALL OF OUR PRODUCTS ARE CAREFULLY<br>DESIGNED AND CRAFTED WITH YOUR FAMILY IN MIND.</p>
  </div>

  <div class="brand-mark"><span class="dot"></span>Serene Grove</div>
  <div class="web-tab">www.SereneGrove.com</div>
</section>

</body>
</html>
```